This is a book by, for and about bereaved parents and grandparents

I need a paperback size cover with front and back please...I have an example of a cover i had done myself and you will see a butterfly graphic within my Preface (My Story) which may be nice to include..or not.

Please feel free to explore your own psyche on this subject light and dark work accepted...love to see your concepts on this difficult subject.
thanks and good luck to you all!
Updates

Good Day Designer..I will post my current photo for the cover shortly and i cannot wait to see your great designs!

Apologies to you all for the delay in providing feedback ..I'm a little overwhelmed at the quality of your work and most likely will be adding a second and third place tonight when i finalize this project..thanks for your hard work and patience

thanks to all the designers for your heartfelt work on this project..it is so very personal to me and If i could afford it I'd pay you all ..do take care and thanks again for your submisions Marla .

https://www.quillnest.com/Lanterns-Along-the-Quiet-Shore-4837201956310482/?epa=SEARCH_BOX

Target Market(s)

Family of children who have died before their time especially those who've left parents and grandparents to grieve their loss of all ages.

Industry/Entity Type

Writer

Font styles to use
Serif
Sans Serif
Decorative
Script

Colors

Designer to choose colors to be used in the design.

Requirements
Must have
• feeling of loss and renewal important to end in hope and faith for future despite the years and months and days of pure agony
• my pic
• my name to be seen clearly on front of paperback
Nice to have
• maybe my butterfly graphic if it works with your concept?
• I would appreciate it if you read my Preface it 23 pages but I hope it will provide insight into the contents of the book thanks for your time and patience
Should not have
• Gravestones religous icons
• such as crosses etc

```html
<!DOCTYPE html>
<html lang="en">
<head>
<meta charset="utf-8">
<title>Lanterns Along the Quiet Shore — Cover</title>
<link rel="stylesheet" href="https://fonts.googleapis.com/css2?family=Oswald:wght@300;400;500&display=swap">
<style>
  :root {
    --stage: #e4e4e4;
    --teal-mid: #2f7f72;
    --teal-deep: #0e5656;
    --teal-dark: #0a4a4c;
    --gold: #f3d37f;
    --gold-rule: #b99d55;
    --white: #f5f5f2;
  }
  * { margin: 0; padding: 0; box-sizing: border-box; }
  html, body {
    width: 1200px; height: 1200px; overflow: hidden;
    background: radial-gradient(circle at 50% 50%, #f4f4f4 0%, var(--stage) 70%, #d2d2d2 100%);
  }
  .cover {
    position: absolute; left: 220px; top: 30px;
    width: 760px; height: 1140px; overflow: hidden;
    background:
      radial-gradient(ellipse 60% 30% at 50% 4%, rgba(255,214,90,0.95) 0%, rgba(230,190,70,0.55) 45%, rgba(120,150,80,0) 100%),
      linear-gradient(180deg, #b3a442 0%, #6f9a5e 22%, var(--teal-mid) 42%, #1f6e68 65%, var(--teal-deep) 85%, var(--teal-dark) 100%);
    font-family: "Oswald", "Arial Narrow", sans-serif;
    box-shadow: 0 10px 30px rgba(0,0,0,0.18);
  }
  .halo-ring {
    position: absolute; left: 70px; top: 70px; width: 620px; height: 150px;
  }
  .author-photo {
    position: absolute; left: 290px; top: 0; width: 190px; height: 270px;
    background: linear-gradient(180deg, #8a7a4e 0%, #cbb897 35%, #e9dcc0 60%, rgba(200,190,150,0) 100%);
    opacity: 0.85;
    -webkit-mask-image: radial-gradient(ellipse 60% 70% at 50% 40%, #000 55%, transparent 100%);
            mask-image: radial-gradient(ellipse 60% 70% at 50% 40%, #000 55%, transparent 100%);
  }
  .title {
    position: absolute; left: 0; top: 0; width: 760px; height: 910px;
  }
  .title-text {
    font-family: "Oswald", "Arial Narrow", sans-serif;
    font-weight: 400; fill: var(--gold); text-anchor: middle;
  }
  .title-lead { font-size: 46px; letter-spacing: 1px; }
  .title-big { font-size: 220px; letter-spacing: 2px; }
  .title-mid { font-size: 172px; letter-spacing: 6px; }
  .title-link { font-size: 40px; }
  .rule {
    position: absolute; left: 58px; right: 58px; top: 912px;
    height: 1px; background: var(--gold-rule);
  }
  .subtitle {
    position: absolute; left: 0; right: 0; top: 930px;
    text-align: center; color: var(--gold);
    font-weight: 400; font-size: 21px; line-height: 1.3; letter-spacing: 0.6px; text-transform: uppercase;
  }
  .author {
    position: absolute; left: 0; right: 0; top: 1015px;
    text-align: center; color: var(--white);
    font-weight: 300; font-size: 72px; line-height: 1; letter-spacing: 1px; text-transform: uppercase;
  }
</style>
</head>
<body>
  <main class="cover">
    <svg class="halo-ring" viewBox="0 0 620 150" aria-hidden="true">
      <ellipse cx="310" cy="75" rx="305" ry="68" fill="none" stroke="rgba(255,245,210,0.45)" stroke-width="3"/>
    </svg>
    <div class="author-photo" role="img" aria-label="Author photo: an adult embracing a young person, seen from behind, bathed in golden light"></div>

    <svg class="title" viewBox="0 0 760 910" role="heading" aria-level="1" aria-label="Lanterns Along the Quiet Shore">
      <defs>
        <linearGradient id="wing-tone" x1="0" y1="0" x2="0" y2="1">
          <stop offset="0" stop-color="#e8e8e8"/>
          <stop offset="0.6" stop-color="#d4d4d4"/>
          <stop offset="1" stop-color="#9a9a9a"/>
        </linearGradient>
      </defs>
      <text class="title-text title-lead" x="380" y="272">LANTERNS</text>
      <text class="title-text title-big" x="380" y="470">ALONG</text>
      <g role="img" aria-label="White and silver butterfly illustration with dark grey wing tips">
        <rect x="235" y="405" width="290" height="230" rx="40" fill="url(#wing-tone)" opacity="0.92"/>
      </g>
      <text class="title-text title-link" x="380" y="505">THE</text>
      <text class="title-text title-mid" x="380" y="738">QUIET</text>
      <text class="title-text title-mid" x="380" y="890">SHORE</text>
    </svg>

    <div class="rule"></div>
    <p class="subtitle">Grieving the death of a child in an open and healthy way</p>
    <p class="author">Marla Ashby Corwen</p>
  </main>
</body>
</html>
```